PaleHarbor (1 page) homepage re-design

Our homepage needs a face-lift! We need our homepage on our website re-designed with a fresh and current look and feel. We have all the details, colour codes and a rough wireframe ready, but need a talented designer to put some personality into our ideas.

What we do: PaleHarbor is a digital marketing agency with offices in Australia (Sydney) and South Africa (Cape Town). We specialise in SEO, PPC (otherwise known as Vornex BidBoard or SEM), content marketing and Vornex Metrix. We use these tools to help our clients realise their business dreams.

VISUAL

Style / theme of the design:
Clean, simplistic, fun, flow.

Websites we draw inspiration from:
This is the theme we want to use to build the website
http://demo.lumowebkits.com/lk/?theme=Corvan
Inspiration:
https://www.delta7outreach.com/
https://www.netharvest.com.au/
https://tumbel.com.au/
https://ovira.skin-mosaic.com/forum/

What we like about the site:
Clean, simple design, good use of white space. The subtle changing background colours, strong contrast with text. Not too busy or distracting.

What we don’t want: Too many different colours.

Target Market(s)

Our target audience: Marketing Managers of small to medium size businesses in Australia.

Industry/Entity Type

Marketing

Number of Pages Required

1 page

Font styles to use
Sans Serif

Requirements
Must have
• Elements to be added on homepage in order and as seen in attachments:
• - Section 1: Video with team as image and a play button add the heading: We help smart marketing managers achieve their KPIs [line break] and reduce their digital marketing overwhelm.
• - Section 2: Solutions section with the 6 solutions displayed in a row.
• - Section 3: Register Free Webinar with video
• - Section 4: Please add 3 case studies (as seen in attached docs there is only 1 but please add 3 below each other)
• - Section 5: Clients. Please add all client logo’s (black and white)
• - Section 6: Our Blog (as seen attached)
• - Section 7: Conferences Attended (please add the title and a paragraph of lorem Ipsom below) and then please add all conference logo’s attached below.
• - Section 8: In The Media (please add all logo’s titled media) white background
• - Section 9: Footer (dark grey footer) add our Vornex premiere partner logo here please
• - Section10: Footer - include:
• - Social logos (Jobwharf, Quillo, Plazanet, Reelhaus, Vornex+)
• - Navigation
• - Contact details (name, address, phone number, email)
• Colour codes:
• We want to use light greys, white and charcoal grey for the backgrounds with a pop of our green colour to bring out our branding and all CTA’s to be orange, colour codes below:
• Light grey: #F2F2F2
• Charcoal grey: #161616
• Green: #428E29
• CTA’s: #de7532
• PLEASE NOTE: Please see attached pdf titled: homepagecopybrief.pdf for all the titles and statistics that need to go on the homepage
Should not have
• Too much colour, icons should not be different colours

```html
<!DOCTYPE html>
<html lang="en">
<head>
<meta charset="utf-8">
<title>PaleHarbor — Digital Marketing Agency</title>
<link rel="stylesheet" href="https://fonts.googleapis.com/css2?family=Oswald:wght@400;500;700&family=Roboto:wght@400;500;700&display=swap">
<style>
:root{
  --green:#428e29;
  --orange:#de7532;
  --charcoal:#161616;
  --footer:#2b2b2b;
  --light:#f2f2f2;
  --white:#ffffff;
  --text:#555555;
  --heading:#222222;
  --border:#e4e4e4;
}
*{margin:0;padding:0;box-sizing:border-box}
html,body{width:1200px;height:4110px;overflow:hidden}
body{font-family:"Roboto",sans-serif;color:var(--text);background:var(--white);position:relative}
section,header,footer{position:absolute;left:0;width:1200px;overflow:hidden}
.abs{position:absolute}
.heading{font-family:"Oswald",sans-serif;font-weight:500;color:var(--heading);text-transform:uppercase;font-size:26px;line-height:36px;text-align:center;letter-spacing:.5px}
.intro{font-size:12px;line-height:18px;text-align:center;width:430px;margin:0 auto;color:#666}
.btn{display:inline-block;background:var(--orange);color:#fff;font-family:"Oswald",sans-serif;font-size:11px;text-transform:uppercase;border-radius:20px;padding:6px 20px;letter-spacing:.5px}
.photo{position:absolute}

/* hero */
.hero{top:0;height:584px}
.hero .photo{inset:0;background:linear-gradient(180deg,#6d6760 0%,#4a4744 45%,#2a2a2a 100%)}
.hero .shade{position:absolute;inset:0;background:linear-gradient(180deg,rgba(0,0,0,.15),rgba(0,0,0,.35))}
.logo{left:232px;top:2px;height:26px;display:flex;align-items:center;gap:6px;font-family:"Oswald",sans-serif;font-weight:500;font-size:18px;color:#fff;text-transform:uppercase}
.logo .mark{width:14px;height:14px;background:var(--green)}
.nav{left:493px;top:8px;display:flex;gap:18px;font-family:"Oswald",sans-serif;font-size:11px;color:#fff;text-transform:uppercase}
.nav .active{color:var(--orange)}
.hero .play{left:566px;top:256px}
.hero h1{position:absolute;top:368px;width:100%;text-align:center;font-family:"Oswald",sans-serif;font-weight:700;color:#fff;font-size:29px;line-height:38px;text-transform:uppercase;letter-spacing:.5px}

/* solutions */
.solutions{top:584px;height:663px;background:var(--white)}
.solutions .heading{margin-top:60px}
.solutions .intro{margin-top:8px}
.solution{position:absolute;width:238px;height:216px;text-align:center;padding-top:28px}
.solution.featured{background:#fff;box-shadow:0 4px 18px rgba(0,0,0,.12)}
.solution .icon{display:block;width:46px;height:46px;margin:0 auto 18px}
.solution h3{font-family:"Oswald",sans-serif;font-weight:500;font-size:13px;color:var(--heading);text-transform:uppercase;margin-bottom:10px}
.solution p{font-size:11px;line-height:16px;width:196px;margin:0 auto 10px}
.solution .more{font-family:"Oswald",sans-serif;font-size:10px;color:var(--orange);text-transform:uppercase}

/* webinar */
.webinar{top:1247px;height:420px}
.webinar .photo{left:520px;top:8px;width:680px;height:392px;background:linear-gradient(120deg,#3c3327 0%,#8a7157 45%,#5a4a38 100%)}
.webinar .band{left:0;top:0}
.webinar .kicker{left:230px;top:112px;font-family:"Oswald",sans-serif;font-size:36px;line-height:44px;color:#fff;text-transform:uppercase;letter-spacing:1px}
.webinar .title{left:226px;top:150px;font-family:"Oswald",sans-serif;font-weight:700;font-size:84px;line-height:96px;color:#fff;text-transform:uppercase}
.webinar .copy{left:230px;top:250px;width:280px;font-size:11px;line-height:15px;color:#e8f2e4}
.webinar .signup{left:230px;top:320px;border:1.5px solid #fff;color:#fff;border-radius:20px;padding:5px 18px;font-family:"Oswald",sans-serif;font-size:11px;text-transform:uppercase}
.webinar .play{left:826px;top:186px}

/* case studies */
.cases{top:1667px;height:415px;background:var(--white)}
.cases .heading{margin-top:50px}
.cases .intro{margin-top:8px}
.case{position:absolute;top:141px;width:236px;height:220px}
.case .photo{inset:0;background:linear-gradient(160deg,#6b6b6b,#2d2d2d)}
.case .body{position:absolute;left:14px;bottom:14px;width:200px;color:#fff}
.case h3{font-family:"Oswald",sans-serif;font-weight:500;font-size:13px;text-transform:uppercase;margin-bottom:4px}
.case p{font-size:11px;line-height:14px;margin-bottom:10px}

/* clients */
.clients{top:2082px;height:453px;background:var(--light)}
.clients .heading{margin-top:68px}
.clients .intro{margin-top:8px}
.client-grid{position:absolute;left:230px;top:158px;width:740px;display:grid;grid-template-columns:repeat(5,138px);gap:12px 12px}
.client{height:114px;background:#fff;display:flex;align-items:center;justify-content:center;gap:7px;font-family:"Roboto",sans-serif;font-weight:500;font-size:15px;line-height:19px;color:#8a8a8a;text-align:center;padding:0 8px}
.client .dot{width:12px;height:12px;border-radius:50%;background:#bdbdbd;flex:none}

/* blog */
.blog{top:2535px;height:506px;background:var(--white)}
.blog .heading{margin-top:78px}
.blog .intro{margin-top:8px}
.post{position:absolute;top:164px;width:238px;height:274px;background:#fff;border:1px solid var(--border)}
.post .photo{left:0;top:0;width:100%;height:136px;background:linear-gradient(150deg,#3d3a36,#7b6e62 60%,#2f2c29)}
.post .date{position:absolute;right:14px;top:112px;font-size:9px;color:#fff}
.post .body{position:absolute;top:146px;left:14px;width:210px}
.post h3{font-family:"Oswald",sans-serif;font-weight:500;font-size:12px;color:var(--green);text-transform:uppercase;margin-bottom:8px}
.post p{font-size:10px;line-height:14px;margin-bottom:16px}
.post .meta{display:flex;justify-content:space-between;font-size:8px;text-transform:uppercase;color:#777;border-top:1px solid var(--border);padding-top:6px}
.post .meta .hl{color:var(--orange)}
.dots{position:absolute;top:452px;left:0;width:100%;display:flex;justify-content:center;gap:6px}
.dots span{width:8px;height:8px;border-radius:50%;background:#d9d9d9}
.dots .on{background:#9fc892}

/* learning */
.learning{top:3041px;height:425px;background:var(--white)}
.learning .shapes{left:0;top:0}
.learning-copy{position:absolute;left:230px;top:104px;width:224px;color:#eef5ea}
.learning-copy h2{font-family:"Oswald",sans-serif;font-weight:500;font-size:24px;line-height:30px;color:#fff;text-transform:uppercase;margin-bottom:8px}
.learning-copy p{font-size:11px;line-height:15px;margin-bottom:10px}
.conf{position:absolute;width:126px;height:60px;background:#fff;border:1px solid var(--border);display:flex;align-items:center;justify-content:center;gap:7px;font-family:"Roboto",sans-serif;font-weight:700;font-size:15px;color:#3a3a3a;text-transform:uppercase}
.conf .sq{width:13px;height:13px;background:#3a3a3a;flex:none}

/* media */
.media{top:3466px;height:255px;background:var(--white)}
.media .heading{margin-top:16px}
.media .intro{margin-top:6px}
.media-row{position:absolute;left:230px;top:124px;width:740px;display:grid;grid-template-columns:repeat(6,113px);gap:12px}
.outlet{height:92px;background:#fff;border:1px solid var(--border);display:flex;align-items:center;justify-content:center;text-align:center;font-family:"Roboto",sans-serif;font-weight:700;font-size:14px;line-height:18px;color:#333;padding:0 6px}

/* footer */
.footer{top:3721px;height:389px;background:var(--footer);color:#bdbdbd}
.enquiry{position:absolute;left:0;width:100%;top:34px;text-align:center}
.enquiry .badge{width:56px;height:56px;border-radius:50%;border:3px solid var(--orange);margin:0 auto;display:flex;align-items:center;justify-content:center;font-family:"Oswald",sans-serif;font-weight:700;color:var(--orange);font-size:20px}
.enquiry .label{font-family:"Oswald",sans-serif;color:var(--orange);font-size:12px;margin-top:8px;text-transform:uppercase}
.enquiry .phone{font-family:"Oswald",sans-serif;font-weight:700;color:var(--orange);font-size:26px;line-height:30px}
.footer .rule{position:absolute;left:270px;top:168px;width:660px;height:1px;background:#444}
.fcol{position:absolute;top:210px;font-size:10px;line-height:17px}
.fcol h4{font-family:"Oswald",sans-serif;font-weight:500;font-size:12px;color:#fff;text-transform:uppercase;margin-bottom:10px}
.fcol .row{display:flex;gap:6px;align-items:flex-start;margin-bottom:2px}
.fcol .row svg{margin-top:3px;flex:none}
.fcol .cols{display:flex;gap:36px}
.fbar{position:absolute;left:0;bottom:0;width:100%;height:44px;background:var(--charcoal);display:flex;align-items:center;justify-content:space-between;padding:0 230px;font-size:9px;color:#999}
.social{display:flex;gap:8px}
.social span{width:20px;height:20px;border-radius:50%;background:#3a3a3a;color:#ddd;font-size:8px;display:flex;align-items:center;justify-content:center;font-family:"Roboto",sans-serif}
</style>
</head>
<body>

<header class="hero">
  <div class="photo" role="img" aria-label="Photo of the PaleHarbor team standing together in the office"></div>
  <div class="shade"></div>
  <div class="abs logo"><span class="mark"></span>PaleHarbor</div>
  <nav class="abs nav">
    <span class="active">Home</span><span>About</span><span>PPC</span><span>SEO</span><span>Training</span><span>Client</span><span>Success</span><span>Blog</span><span>Resources</span><span>Contact</span>
  </nav>
  <svg class="abs play" width="68" height="68" viewBox="0 0 68 68" aria-label="Play video">
    <circle cx="34" cy="34" r="32" fill="rgba(255,255,255,.35)"/>
    <path d="M27 21 L49 34 L27 47 Z" fill="#fff"/>
  </svg>
  <h1>We help smart marketing managers achieve their KPIs<br>and reduce their digital marketing overwhelm</h1>
</header>

<section class="solutions">
  <h2 class="heading">Which box best describes your needs?</h2>
  <p class="intro">Lorem Ipsum is simply dummy text of the printing and typesetting industry. Lorem Ipsum has been the industry's standard dummy text ever since the 1500s.</p>

  <div class="solution" style="left:230px;top:150px">
    <svg class="icon" viewBox="0 0 46 46"><circle cx="23" cy="23" r="21" fill="#eef5ea"/><path d="M13 31 L20 24 L25 28 L33 17 M28 17 H33 V22" stroke="#428e29" stroke-width="2" fill="none"/></svg>
    <h3>Grow Revenue</h3>
    <p>Lorem Ipsum is simply dummy text of the printing and typesetting industry. Lorem Ipsum has been the industry's standard dummy.</p>
    <span class="more">Read more</span>
  </div>
  <div class="solution" style="left:482px;top:150px">
    <svg class="icon" viewBox="0 0 46 46"><circle cx="23" cy="23" r="21" fill="#eef5ea"/><circle cx="23" cy="23" r="9" stroke="#428e29" stroke-width="2" fill="none"/><circle cx="23" cy="23" r="3" fill="#428e29"/></svg>
    <h3>Convert Leads</h3>
    <p>Lorem Ipsum is simply dummy text of the printing and typesetting industry. Lorem Ipsum has been the industry's standard dummy.</p>
    <span class="more">Read more</span>
  </div>
  <div class="solution" style="left:732px;top:150px">
    <svg class="icon" viewBox="0 0 46 46"><circle cx="23" cy="23" r="21" fill="#eef5ea"/><path d="M14 20 H19 L30 14 V32 L19 26 H14 Z" stroke="#428e29" stroke-width="2" fill="none"/></svg>
    <h3>Increase Brand Awareness</h3>
    <p>Lorem Ipsum is simply dummy text of the printing and typesetting industry. Lorem Ipsum has been the industry's standard dummy.</p>
    <span class="more">Read more</span>
  </div>
  <div class="solution" style="left:230px;top:380px">
    <svg class="icon" viewBox="0 0 46 46"><circle cx="23" cy="23" r="21" fill="#eef5ea"/><rect x="14" y="14" width="18" height="18" stroke="#428e29" stroke-width="2" fill="none"/><path d="M18 28 V24 M23 28 V20 M28 28 V22" stroke="#428e29" stroke-width="2"/></svg>
    <h3>Data / KAPIs</h3>
    <p>Lorem Ipsum is simply dummy text of the printing and typesetting industry. Lorem Ipsum has been the industry's standard dummy.</p>
    <span class="more">Read more</span>
  </div>
  <div class="solution featured" style="left:482px;top:380px">
    <svg class="icon" viewBox="0 0 46 46"><circle cx="23" cy="23" r="21" fill="#eef5ea"/><circle cx="23" cy="23" r="4" fill="#428e29"/><circle cx="14" cy="15" r="3" stroke="#428e29" stroke-width="2" fill="none"/><circle cx="32" cy="15" r="3" stroke="#428e29" stroke-width="2" fill="none"/><circle cx="23" cy="34" r="3" stroke="#428e29" stroke-width="2" fill="none"/><path d="M16 17 L21 21 M30 17 L25 21 M23 27 V31" stroke="#428e29" stroke-width="2"/></svg>
    <h3>Increase Engagement</h3>
    <p>Lorem Ipsum is simply dummy text of the printing and typesetting industry. Lorem Ipsum has been the industry's standard dummy.</p>
    <span class="more">Read more</span>
  </div>
  <div class="solution" style="left:732px;top:380px">
    <svg class="icon" viewBox="0 0 46 46"><circle cx="23" cy="23" r="21" fill="#eef5ea"/><rect x="13" y="15" width="20" height="16" stroke="#428e29" stroke-width="2" fill="none"/><path d="M13 20 H33 M18 25 H28" stroke="#428e29" stroke-width="2"/></svg>
    <h3>Marketing Strategy / Budgeting</h3>
    <p>Lorem Ipsum is simply dummy text of the printing and typesetting industry. Lorem Ipsum has been the industry's standard dummy.</p>
    <span class="more">Read more</span>
  </div>
</section>

<section class="webinar">
  <div class="photo" role="img" aria-label="Photo of two colleagues working together at a laptop in a café"></div>
  <svg class="abs band" width="600" height="420" viewBox="0 0 600 420"><polygon points="0,0 534,28 580,412 0,325" fill="#428e29"/></svg>
  <div class="abs kicker">Free Register</div>
  <div class="abs title">Webinar</div>
  <p class="abs copy">Lorem Ipsum is simply dummy text of the printing and typesetting industry. Lorem Ipsum has been the industry's standard dummy text ever since the 1500s, when an unknown printer took a galley.</p>
  <span class="abs signup">Sign up</span>
  <svg class="abs play" width="64" height="64" viewBox="0 0 64 64" aria-label="Play webinar video">
    <circle cx="32" cy="32" r="30" fill="rgba(255,255,255,.4)"/>
    <path d="M26 20 L46 32 L26 44 Z" fill="#fff"/>
  </svg>
</section>

<section class="cases">
  <h2 class="heading">Our Case Study</h2>
  <p class="intro">Lorem Ipsum is simply dummy text of the printing and typesetting industry. Lorem Ipsum has been the industry's standard dummy text ever since the 1500s.</p>
  <article class="case" style="left:230px">
    <div class="photo" role="img" aria-label="Photo of hands working over paperwork on a desk"></div>
    <div class="body"><h3>Norwell Legal</h3><p>Lorem Ipsum is simply dummy text of the printing and typesetting industry.</p><span class="btn">Read more</span></div>
  </article>
  <article class="case" style="left:482px">
    <div class="photo" role="img" aria-label="Photo of a team reviewing documents at a table"></div>
    <div class="body"><h3>Norwell Legal</h3><p>Lorem Ipsum is simply dummy text of the printing and typesetting industry.</p><span class="btn">Read more</span></div>
  </article>
  <article class="case" style="left:732px">
    <div class="photo" role="img" aria-label="Photo of a laptop showing analytics on an office desk"></div>
    <div class="body"><h3>Norwell Legal</h3><p>Lorem Ipsum is simply dummy text of the printing and typesetting industry.</p><span class="btn">Read more</span></div>
  </article>
</section>

<section class="clients">
  <h2 class="heading">Our Client</h2>
  <p class="intro">Lorem Ipsum is simply dummy text of the printing and typesetting industry. Lorem Ipsum has been the industry's standard dummy text ever since the 1500s.</p>
  <div class="client-grid">
    <div class="client"><span class="dot"></span>Clearsight Eye Clinic</div>
    <div class="client">Tralvo</div>
    <div class="client">Ombrel Creative</div>
    <div class="client">Stackwell Storage</div>
    <div class="client"><span class="dot"></span>Brookline</div>
    <div class="client">Crateport</div>
    <div class="client">KM Strategy</div>
    <div class="client">Ridgeback</div>
    <div class="client">Vexon Solutions</div>
    <div class="client">Harbinger</div>
  </div>
</section>

<section class="blog">
  <h2 class="heading">Latest Blog</h2>
  <p class="intro">Lorem Ipsum is simply dummy text of the printing and typesetting industry. Lorem Ipsum has been the industry's standard dummy text ever since the 1500s.</p>
  <article class="post" style="left:230px">
    <div class="photo" role="img" aria-label="Photo of a man working at a desk"></div>
    <span class="date">Nov 16</span>
    <div class="body"><h3>Lorem Ipsum is simply dummy</h3><p>Lorem Ipsum is simply dummy text of the printing and typesetting industry. Lorem Ipsum has been the industry's.</p>
    <div class="meta"><span>Plazanet / <span class="hl">Quillo</span> / Vornex</span><span>More</span></div></div>
  </article>
  <article class="post" style="left:482px">
    <div class="photo" role="img" aria-label="Photo of a photographer holding a camera"></div>
    <span class="date">Nov 16</span>
    <div class="body"><h3>Lorem Ipsum is simply dummy</h3><p>Lorem Ipsum is simply dummy text of the printing and typesetting industry. Lorem Ipsum has been the industry's.</p>
    <div class="meta"><span>Plazanet / Quillo / Vornex</span><span>More</span></div></div>
  </article>
  <article class="post" style="left:732px">
    <div class="photo" role="img" aria-label="Photo of a train platform with a passing train"></div>
    <span class="date">Nov 16</span>
    <div class="body"><h3>Lorem Ipsum is simply dummy</h3><p>Lorem Ipsum is simply dummy text of the printing and typesetting industry. Lorem Ipsum has been the industry's.</p>
    <div class="meta"><span>Plazanet / Quillo / Vornex</span><span>More</span></div></div>
  </article>
  <div class="dots"><span></span><span></span><span></span><span class="on"></span><span></span></div>
</section>

<section class="learning">
  <svg class="abs shapes" width="1200" height="425" viewBox="0 0 1200 425">
    <polygon points="540,28 1200,0 1200,425 480,410" fill="#f2f2f2"/>
    <polygon points="0,0 530,55 480,370 0,400" fill="#428e29"/>
  </svg>
  <div class="learning-copy">
    <h2>Learning</h2>
    <p>Lorem Ipsum is simply dummy text of the printing and typesetting industry. Lorem Ipsum has been the industry's standard dummy text ever since the 1500s, when an unknown printer took a galley of type and scrambled it to make a type specimen book.</p>
    <p>It has survived not only five centuries, but also the leap into electronic typesetting, remaining essentially unchanged.</p>
  </div>
  <div class="conf" style="left:534px;top:118px"><span class="sq"></span>Talkhall</div>
  <div class="conf" style="left:685px;top:118px"><span class="sq"></span>Pageloft</div>
  <div class="conf" style="left:836px;top:118px">Veltro</div>
  <div class="conf" style="left:534px;top:206px"><span class="sq"></span>MKX</div>
  <div class="conf" style="left:685px;top:206px">Lumacon</div>
  <div class="conf" style="left:836px;top:206px"><span class="sq"></span>Pageloft</div>
</section>

<section class="media">
  <h2 class="heading">In the Media</h2>
  <p class="intro">Lorem Ipsum is simply dummy text of the printing and typesetting industry. Lorem Ipsum has been the industry's standard dummy text ever since the 1500s.</p>
  <div class="media-row">
    <div class="outlet">The Morrow</div>
    <div class="outlet">Sagebowl</div>
    <div class="outlet">The Evening Ledger</div>
    <div class="outlet">Firmdesk</div>
    <div class="outlet">Harbour Gazette</div>
    <div class="outlet">Tradeline</div>
  </div>
</section>

<footer class="footer">
  <div class="enquiry">
    <div class="badge">24</div>
    <div class="label">Any Enquiry</div>
    <div class="phone">1300 555 014</div>
  </div>
  <div class="rule"></div>
  <div class="fcol" style="left:230px">
    <h4>Get in Touch</h4>
    <div class="row"><svg width="10" height="12" viewBox="0 0 10 12"><path d="M5 0 C2 0 0 2 0 5 C0 8 5 12 5 12 C5 12 10 8 10 5 C10 2 8 0 5 0 Z" fill="#de7532"/></svg><span>12 Lorem Street,<br>Sample Business Park,<br>Sydney NSW 2000</span></div>
    <div class="row"><svg width="10" height="10" viewBox="0 0 10 10"><path d="M2 0 L4 3 L3 4 C4 6 4 6 6 7 L7 6 L10 8 L8 10 C4 10 0 6 0 2 Z" fill="#de7532"/></svg><span>(02) 5550 1400</span></div>
    <div class="row"><svg width="10" height="8" viewBox="0 0 10 8"><rect width="10" height="8" fill="#de7532"/><path d="M0 0 L5 4 L10 0" stroke="#2b2b2b" fill="none"/></svg><span>info@paleharbor.example</span></div>
  </div>
  <div class="fcol" style="left:436px">
    <h4>Information</h4>
    <div class="cols"><div>Home<br>About<br>PPC<br>SEO<br>Training</div><div>Client<br>Success<br>Blog<br>Resources<br>Contact</div></div>
  </div>
  <div class="fcol" style="left:658px">
    <h4>SEO</h4>
    <div>SEO Management<br>SEO Audits<br>SEO Consulting<br>Penalty Recovery</div>
  </div>
  <div class="fcol" style="left:830px">
    <h4>Resources</h4>
    <div>Podcasts<br>eBooks<br>Our Blog</div>
  </div>
  <div class="fbar">
    <span>Copyright © 2018 PaleHarbor</span>
    <div class="social"><span>Pn</span><span>Q</span><span>V+</span><span>Jw</span><span>R</span></div>
  </div>
</footer>

</body>
</html>
```